Its time for a new website

We are at a point now where we are in desperate need of a new website. It was last updated 2006 but still looks like its 1995. We are looking for something eye catching to our clients but easy to navigate and add/remove photos of jobs/trucks and information. Our key business is the manufacture of fire appliances and resale of parts and equipment.

www.dunmorerescue.com.au

Coding

Coded - Design and coding required

Number of Pages Required

5+ page

Requirements
Must have
• Logo

```html
<!DOCTYPE html>
<html lang="en">
<head>
<meta charset="utf-8">
<title>Dunmore Rescue – Fire Appliance Manufacturer</title>
<link rel="stylesheet" href="https://fonts.googleapis.com/css2?family=Open+Sans:wght@400;600;700&family=Play:wght@400;700&display=swap">
<style>
:root{
  --blue:#0a8ad0;
  --red:#b41f24;
  --red-dark:#8e1418;
  --ink:#222;
  --dark:#2d2d2d;
  --grey:#ededed;
  --grey-line:#9a9a9a;
  --text:#555;
  --white:#fff;
}
*{box-sizing:border-box;margin:0;padding:0}
html,body{width:1200px;height:2769px;overflow:hidden}
body{position:relative;background:var(--white);font-family:"Open Sans",Arial,sans-serif;color:var(--text)}
.abs{position:absolute}

/* top bar */
.topbar{top:0;left:0;width:1200px;height:37px;background:var(--blue);color:var(--white);font-size:13px}
.topbar .mail{position:absolute;right:195px;top:10px;display:flex;align-items:center;gap:8px}
.topbar .social{position:absolute;right:55px;top:9px;display:flex;gap:12px;padding-left:16px;border-left:1px solid rgba(255,255,255,.6)}
.social span{display:block;width:18px;height:18px;border-radius:3px;background:currentColor;opacity:.9}

/* header */
.header{top:37px;left:0;width:1200px;height:87px}
.brand{position:absolute;left:100px;top:18px;display:flex;align-items:center;gap:12px}
.brand-mark{width:48px;height:48px;border-radius:50%;background:var(--red)}
.brand-name{font-family:"Play",sans-serif;font-weight:700;font-size:24px;color:var(--blue)}
.helpline{position:absolute;right:97px;top:22px;display:flex;align-items:center;gap:12px}
.helpline .ring{width:42px;height:42px;border-radius:50%;border:2px solid var(--blue);display:flex;align-items:center;justify-content:center}
.helpline small{display:block;font-size:13px;color:#444}
.helpline strong{display:block;font-size:18px;font-weight:400;color:var(--ink)}

/* nav */
.nav{top:124px;left:0;width:1200px;height:51px;background:var(--red);display:flex;padding-left:101px}
.nav a{color:var(--white);text-decoration:none;font-family:"Play",sans-serif;font-weight:700;font-size:15px;line-height:51px;padding:0 11px}
.nav a.active{background:var(--red-dark)}

/* hero */
.hero{top:175px;left:0;width:1200px;height:440px;background:linear-gradient(100deg,#5a4a2c 0%,#8a2a22 25%,#c8cfd6 50%,#9ba9a3 70%,#5a7a3a 100%)}
.hero-caption{position:absolute;top:250px;left:310px;width:790px;height:105px}
.hero-caption svg{position:absolute;inset:0}
.hero-caption p{position:absolute;color:var(--white);font-family:"Play",sans-serif;font-weight:700;font-size:28px;letter-spacing:.3px}
.dots{position:absolute;top:405px;left:566px;display:flex;gap:12px}
.dots i{width:13px;height:13px;border-radius:50%;background:var(--white)}
.dots i.on{background:var(--red)}

/* ticker */
.ticker{top:615px;left:0;width:1200px;height:86px;background:var(--blue);color:var(--white);font-size:17px;text-align:center;line-height:86px}
.ticker svg{position:absolute;top:30px}

/* section titles */
.section-title{left:50%;transform:translateX(-50%);height:46px}
.section-title svg{position:absolute;inset:0}
.section-title h2{position:relative;font-family:"Play",sans-serif;font-weight:700;font-size:21px;color:var(--white);text-align:center;line-height:46px;letter-spacing:.5px}
.intro{top:820px;left:270px;width:660px;text-align:center;font-size:13px;line-height:26px}

/* service cards */
.card{width:306px;height:345px;background:var(--grey);border:1px solid var(--grey-line)}
.card .photo{position:absolute;top:0;left:0;width:100%;height:240px;border-radius:0 0 50% 50%/0 0 18% 18%}
.card .hex{position:absolute;left:124px;top:210px}
.card h3{position:absolute;top:285px;width:100%;text-align:center;font-family:"Play",sans-serif;font-weight:700;font-size:27px;color:var(--red)}
.card.dark h3{color:var(--ink)}

/* news */
.news{width:306px}
.news .photo{height:176px;border:1px solid #bbb}
.news .meta{position:relative;margin-top:16px;padding-left:56px;height:50px}
.news .date{position:absolute;left:0;top:0}
.news .date span{position:absolute;top:9px;width:46px;text-align:center;color:var(--white);font-size:12px;line-height:14px}
.news h4{font-size:14px;font-weight:700;color:var(--red);text-transform:uppercase}
.news .posted{font-size:12px;color:#666;margin-top:6px;display:flex;align-items:center;gap:8px}
.news p{font-size:12.5px;line-height:20px;text-align:justify;margin-top:2px}
.news .more{position:absolute;right:0;font-size:13px;color:var(--red);display:flex;align-items:center;gap:8px}
.news .more.boxed{border:1px solid var(--red);padding:0 0 0 8px;gap:6px}
.news .more.boxed b{background:var(--red);padding:1px 8px;display:flex}

/* footer band */
.band{top:2237px;left:0;width:1200px;height:85px;background:var(--dark)}
.band .left{position:absolute;left:0;top:0}
.band .brand-small{position:absolute;left:118px;top:18px;display:flex;align-items:center;gap:8px}
.band .brand-small i{width:28px;height:28px;border-radius:50%;background:var(--red)}
.band .brand-small b{font-family:"Play",sans-serif;font-size:15px;color:var(--blue)}
.band .emergency{position:absolute;right:205px;top:30px;color:var(--white);font-family:"Play",sans-serif;font-weight:700;font-size:20px}
.band .social{position:absolute;right:97px;top:31px;display:flex;gap:10px;padding-left:14px;border-left:1px solid #888;color:var(--white)}

/* map */
.map{top:2322px;left:0;width:1200px;height:378px;background:linear-gradient(180deg,#e7e7e7,#dcdcdc)}
.map .pin{position:absolute;left:718px;top:52px}
.address{position:absolute;left:437px;top:170px;width:213px;height:60px;background:var(--white);border:1px solid #999;text-align:center;font-size:13px;line-height:20px;padding-top:9px;color:var(--ink)}
.contact-icons{position:absolute;left:512px;top:237px;display:flex;gap:12px}
.contact-icons span{width:56px;height:50px;display:flex;align-items:center;justify-content:center;background:var(--white);border:1px solid #bbb}
.contact-icons span.on{background:var(--blue);border-color:var(--blue)}

/* bottom bar */
.bottom{top:2700px;left:0;width:1200px;height:69px;background:var(--dark);color:var(--white);font-size:12px;line-height:69px}
.bottom .copy{position:absolute;left:88px}
.bottom nav{position:absolute;right:96px;display:flex;gap:9px}
</style>
</head>
<body>

<div class="abs topbar">
  <div class="mail">
    <svg width="18" height="13" viewBox="0 0 18 13"><rect x="0.5" y="0.5" width="17" height="12" fill="none" stroke="#fff"/><path d="M1 1l8 6 8-6" fill="none" stroke="#fff"/></svg>
    info@dunmorerescue.com.au
  </div>
  <div class="social"><span></span><span></span><span></span></div>
</div>

<header class="abs header">
  <div class="brand"><div class="brand-mark"></div><div class="brand-name">Dunmore Rescue</div></div>
  <div class="helpline">
    <div class="ring"><svg width="20" height="20" viewBox="0 0 24 24"><path d="M6.6 10.8a15 15 0 006.6 6.6l2.2-2.2a1 1 0 011-.25 11.4 11.4 0 003.6.6 1 1 0 011 1V20a1 1 0 01-1 1A17 17 0 013 4a1 1 0 011-1h3.5a1 1 0 011 1c0 1.25.2 2.45.6 3.6a1 1 0 01-.25 1z" fill="#0a8ad0"/></svg></div>
    <div><small>custom helpline</small><strong>08 9555 0142</strong></div>
  </div>
</header>

<nav class="abs nav">
  <a class="active">Home</a><a>About Us</a><a>Pumpers</a><a>Tankers</a><a>GPA/Rescue</a><a>Light Tankers</a><a>Trailers</a><a>Slip-on Units</a><a>NEW for 2006</a><a>Contact Us</a>
</nav>

<section class="abs hero" role="img" aria-label="Firefighters stepping down from a red fire appliance beside a pumper parked in a suburban street">
  <div class="hero-caption">
    <svg width="790" height="105" viewBox="0 0 790 105"><polygon points="20,0 650,0 630,46 0,46" fill="#b41f24" opacity=".9"/><polygon points="120,56 790,56 770,105 100,105" fill="#b41f24" opacity=".9"/></svg>
    <p style="left:25px;top:4px">Western Australia's Largest, most experienced</p>
    <p style="left:126px;top:61px">competent manufacturer of fire fighting vehicles</p>
  </div>
  <div class="dots"><i class="on"></i><i></i><i></i></div>
</section>

<div class="abs ticker">
  <svg style="left:30px" width="16" height="26" viewBox="0 0 16 26"><path d="M14 2L3 13l11 11" fill="none" stroke="#fff" stroke-width="2.5"/></svg>
  Lorem ipsum dolor sit amet, consecte adipiscing elit. Suspendisse condimentum porttitor cursumus. Duis &nbsp;nec nulla turpis.
  <svg style="right:30px" width="16" height="26" viewBox="0 0 16 26"><path d="M2 2l11 11L2 24" fill="none" stroke="#fff" stroke-width="2.5"/></svg>
</div>

<div class="abs section-title" style="top:760px;width:330px">
  <svg width="330" height="46" viewBox="0 0 330 46"><polygon points="0,46 12,0 330,0 318,46" fill="#b41f24"/><polygon points="6,42 16,4 322,4 312,42" fill="#2d2d2d"/></svg>
  <h2>CHECK OUT OUR SERVICE</h2>
</div>
<p class="abs intro">Lorem ipsum dolor sit amet, consecte adipiscing elit. Suspendisse condimentum porttitor cursumus. Duis nec nulla turpis. Nulla lacinia laoreet odio</p>

<svg width="0" height="0" style="position:absolute">
  <defs>
    <g id="hex-icon">
      <polygon points="29,1 55,16 55,46 29,61 3,46 3,16" fill="#fff"/>
      <polygon points="29,6 51,19 51,43 29,56 7,43 7,19" fill="currentColor"/>
      <path d="M20 39v-6a6 6 0 016-6h10m-5-5l6 5-6 5" fill="none" stroke="#fff" stroke-width="2.5"/>
    </g>
  </defs>
</svg>

<div class="abs card" style="top:901px;left:101px">
  <div class="photo" role="img" aria-label="Red pumper fire truck parked on a road" style="background:linear-gradient(160deg,#d8dde0,#b5272a 55%,#8c8f8a)"></div>
  <svg class="hex" width="58" height="62" style="color:#b41f24"><use href="#hex-icon"/></svg>
  <h3>Pumpers</h3>
</div>
<div class="abs card dark" style="top:901px;left:447px">
  <div class="photo" role="img" aria-label="Stainless steel water tanker truck" style="background:linear-gradient(160deg,#6e6e6e,#4a4a4a 60%,#5a5a5a)"></div>
  <svg class="hex" width="58" height="62" style="color:#222"><use href="#hex-icon"/></svg>
  <h3>Tankers</h3>
</div>
<div class="abs card" style="top:901px;left:794px">
  <div class="photo" role="img" aria-label="Red and white general purpose rescue truck outside a fire station" style="background:linear-gradient(160deg,#6e7b55,#c9c9c9 45%,#b5272a 70%,#9aa08c)"></div>
  <svg class="hex" width="58" height="62" style="color:#b41f24"><use href="#hex-icon"/></svg>
  <h3>GPA/Rescue</h3>
</div>

<div class="abs card" style="top:1285px;left:101px">
  <div class="photo" role="img" aria-label="White light tanker with red striping in a garage" style="background:linear-gradient(160deg,#9c8a70,#dcdcdc 50%,#a33 75%,#8d8d8d)"></div>
  <svg class="hex" width="58" height="62" style="color:#b41f24"><use href="#hex-icon"/></svg>
  <h3>Light Tankers</h3>
</div>
<div class="abs card" style="top:1285px;left:447px">
  <div class="photo" role="img" aria-label="Trailer carrying a red water tank and yellow hose reel" style="background:linear-gradient(160deg,#8c7c5a,#d84a4a 45%,#c9b34a 65%,#7a6e5c)"></div>
  <svg class="hex" width="58" height="62" style="color:#b41f24"><use href="#hex-icon"/></svg>
  <h3>Trailers</h3>
</div>
<div class="abs card" style="top:1285px;left:794px">
  <div class="photo" role="img" aria-label="Yellow slip-on firefighting pump unit with hose reel" style="background:linear-gradient(160deg,#7a8a8a,#e0b822 50%,#6e6e6e)"></div>
  <svg class="hex" width="58" height="62" style="color:#b41f24"><use href="#hex-icon"/></svg>
  <h3>Slip-on Units</h3>
</div>

<div class="abs section-title" style="top:1704px;width:265px">
  <svg width="265" height="46" viewBox="0 0 265 46"><polygon points="0,46 12,0 265,0 253,46" fill="#b41f24"/><polygon points="6,42 16,4 257,4 247,42" fill="#2d2d2d"/></svg>
  <h2>LATEST NEWS</h2>
</div>

<svg width="0" height="0" style="position:absolute">
  <defs>
    <polygon id="date-hex" points="23,1 45,13 45,39 23,51 1,39 1,13" fill="#b41f24"/>
  </defs>
</svg>

<article class="abs news" style="top:1780px;left:101px">
  <div class="photo" role="img" aria-label="Firefighters in yellow helmets standing beside an engine" style="background:linear-gradient(120deg,#2b1a16,#7a3a20 40%,#d8b23a 60%,#b5272a)"></div>
  <div class="meta">
    <div class="date"><svg width="46" height="52"><use href="#date-hex"/></svg><span>28<br>May</span></div>
    <h4>Morbi non sem a lacus porta</h4>
    <div class="posted"><svg width="12" height="12"><circle cx="6" cy="6" r="5" fill="none" stroke="#999"/></svg>POSTED &nbsp;29 MAY 2015</div>
  </div>
  <p>Lorem ipsum dolor sit amet, scelerata nunc intuens munus oblitus ait regem orem ipsum</p>
  <a class="more" style="top:337px">Read more <svg width="14" height="10"><path d="M0 5h12M8 1l4 4-4 4" fill="none" stroke="#b41f24"/></svg></a>
</article>

<article class="abs news" style="top:1780px;left:447px">
  <div class="photo" role="img" aria-label="Aerial ladder fire appliances parked in a row with the ladder raised" style="background:linear-gradient(160deg,#5e7a4a,#c9ccd0 40%,#b5272a 70%,#5a5a5a)"></div>
  <div class="meta">
    <div class="date"><svg width="46" height="52"><use href="#date-hex"/></svg><span>24<br>May</span></div>
    <h4>Morbi non sem</h4>
    <div class="posted"><svg width="12" height="12"><circle cx="6" cy="6" r="5" fill="none" stroke="#999"/></svg>POSTED &nbsp;29 MAY 2015</div>
  </div>
  <p>Lorem ipsum dolor sit amet, scelerata nunc intuens munus oblitus ait regem orem ipsum dolor sit amet, scelerata nunc [...]</p>
  <a class="more boxed" style="top:337px">Read more <b><svg width="14" height="10"><path d="M0 5h12M8 1l4 4-4 4" fill="none" stroke="#fff"/></svg></b></a>
</article>

<article class="abs news" style="top:1780px;left:794px">
  <div class="photo" role="img" aria-label="Two firefighters standing in front of a classic red fire engine" style="background:linear-gradient(160deg,#c5c9cc,#b5272a 50%,#6e6e6e)"></div>
  <div class="meta">
    <div class="date"><svg width="46" height="52"><use href="#date-hex"/></svg><span>20<br>May</span></div>
    <h4>Morbi non sem a lacus porta</h4>
    <div class="posted"><svg width="12" height="12"><circle cx="6" cy="6" r="5" fill="none" stroke="#999"/></svg>POSTED &nbsp;29 MAY 2015</div>
  </div>
  <p>Lorem ipsum dolor sit amet, scelerata nunc intuens munus oblitus ait regem</p>
  <a class="more" style="top:337px">Read more <svg width="14" height="10"><path d="M0 5h12M8 1l4 4-4 4" fill="none" stroke="#b41f24"/></svg></a>
</article>

<div class="abs band">
  <svg class="left" width="420" height="85" viewBox="0 0 420 85"><polygon points="0,0 375,0 420,85 0,85" fill="#dedede"/></svg>
  <div class="brand-small"><i></i><b>Dunmore Rescue</b></div>
  <div class="emergency">24/7 Emergency Service: 1-800-555-0199</div>
  <div class="social"><span></span><span></span><span></span></div>
</div>

<div class="abs map" role="img" aria-label="Street map showing the workshop location">
  <svg class="pin" width="44" height="56" viewBox="0 0 44 56"><path d="M22 2a18 18 0 00-18 18c0 14 18 34 18 34s18-20 18-34A18 18 0 0022 2z" fill="#777"/><circle cx="22" cy="20" r="7" fill="#e2e2e2"/></svg>
  <div class="address">Lot 12 Harbour Road<br>Dunmore 6400 Western Australia</div>
  <div class="contact-icons">
    <span class="on"><svg width="22" height="30" viewBox="0 0 22 30"><path d="M11 1a10 10 0 00-10 10c0 8 10 18 10 18s10-10 10-18A10 10 0 0011 1z" fill="none" stroke="#fff" stroke-width="2"/><circle cx="11" cy="11" r="3.5" fill="none" stroke="#fff" stroke-width="2"/></svg></span>
    <span><svg width="32" height="22" viewBox="0 0 32 22"><rect x="1" y="1" width="30" height="20" fill="none" stroke="#333" stroke-width="1.5"/><path d="M1 1l15 11L31 1M1 21l11-10M31 21L20 11" fill="none" stroke="#333" stroke-width="1.5"/></svg></span>
    <span><svg width="26" height="26" viewBox="0 0 24 24"><path d="M6.6 10.8a15 15 0 006.6 6.6l2.2-2.2a1 1 0 011-.25 11.4 11.4 0 003.6.6 1 1 0 011 1V20a1 1 0 01-1 1A17 17 0 013 4a1 1 0 011-1h3.5a1 1 0 011 1c0 1.25.2 2.45.6 3.6a1 1 0 01-.25 1z" fill="none" stroke="#333" stroke-width="1.3"/></svg></span>
  </div>
</div>

<footer class="abs bottom">
  <div class="copy">Dunmore Rescue© 2015. Privacy Policy</div>
  <nav><span>Home</span><span>About Us</span><span>Pumpers</span><span>Tankers</span><span>GPA/Rescue</span><span>Light Tankers</span><span>Trailers</span><span>Slip-on Units</span><span>Contact Us</span></nav>
</footer>

</body>
</html>
```